Harrowgate Estates Business Card for Apartment Buildings

Create business cards for resident managers who run apartment buildings. The audience is the public who are searching for apartment rentals, and current residents who live at the apartment building. Key design element will be incorporating the company logo, however, the logo cannot dominate. The building name and manager name are more important than the logo. Current business card design leaves little room for copy, so we may need to reduce the size on the current card to allow for more space for copy.

Target Market(s)

Adults 18-65 years of age, who are looking for an apartment rental, plus current residents who live at our apartment buildings.

Industry/Entity Type

Property Management

Contact Information for Business Card

A major design element will be use of the company logo. Important property and manager contact information must be part of the design. The size of the logo will need to be reduced to make room for building and manager contact copy.

Font styles to use
Sans Serif

Colors
3176b5
000000
959595
ffffff

Requirements
Must have
• 1) Incorporate the company logo.
• 2) Use the company colors (dark blue, black/grey, over white).
• 3) FEATURE THE BUILDING NAME
• 4) FEATURE THE MANAGER NAME
• 5) The company name is less important than BUILDING and MANAGER
• 6) Manager contact information
• **SEE ATTACHED CREATIVE BRIEF**
Nice to have
• 1) Back of card logo watermark
• 2) Ability to write notes on back of carfd
Should not have
• Avoid letting the company logo dominate the card, the building name and manager are more important than the company logo.

```html
<!DOCTYPE html>
<html lang="en">
<head>
<meta charset="utf-8">
<title>Harrowgate Estates Business Card</title>
<link rel="stylesheet" href="https://fonts.googleapis.com/css2?family=Roboto:wght@400;700;900&display=swap">
<style>
  :root {
    --brand-blue: #3176b5;
    --brand-blue-deep: #1f5f9e;
    --brand-black: #1c1c1c;
    --brand-grey: #959595;
    --brand-white: #ffffff;
    --paper-back: #f1f2f3;
    --watermark: #e2e3e5;
    --stage: #e4e5e7;
  }
  * { box-sizing: border-box; margin: 0; padding: 0; }
  html, body { width: 1200px; height: 780px; overflow: hidden; }
  body {
    background: var(--stage);
    font-family: "Roboto", Arial, sans-serif;
    position: relative;
  }
  .card {
    position: absolute;
    top: 235px;
    width: 540px;
    height: 309px;
    overflow: hidden;
    border-radius: 3px;
    box-shadow: 0 6px 18px rgba(0,0,0,0.18);
  }
  .card--front { left: 40px; background: var(--brand-white); }
  .card--back { left: 620px; background: var(--paper-back); }

  /* Front */
  .front__building {
    position: absolute; left: 40px; right: 40px; top: 40px;
  }
  .building-name {
    color: var(--brand-blue);
    font-weight: 900;
    font-size: 34px;
    line-height: 1;
    letter-spacing: 0.5px;
    white-space: nowrap;
  }
  .building-label {
    color: var(--brand-black);
    font-weight: 700;
    font-size: 13px;
    letter-spacing: 6px;
    margin-top: 8px;
  }
  .front__company {
    position: absolute; left: 40px; top: 130px;
    display: flex; align-items: center; gap: 8px;
  }
  .company-dot {
    width: 12px; height: 12px; border-radius: 50%;
    background: var(--brand-grey);
    flex: none;
  }
  .company-name {
    color: var(--brand-grey);
    font-weight: 700;
    font-size: 12px;
    letter-spacing: 2px;
  }
  .front__nameband {
    position: absolute; left: 0; right: 0; top: 162px; height: 34px;
    background: var(--brand-black);
    color: var(--brand-white);
    display: flex; align-items: center;
    padding-left: 40px;
    font-size: 17px;
  }
  .manager-name { font-weight: 700; letter-spacing: 0.3px; }
  .manager-sep { margin: 0 10px; color: var(--brand-grey); }
  .manager-title { font-weight: 400; font-size: 15px; }
  .front__contact {
    position: absolute; left: 0; right: 0; top: 196px; bottom: 0;
    background: linear-gradient(180deg, var(--brand-blue) 0%, var(--brand-blue-deep) 100%);
    color: var(--brand-white);
    padding: 12px 40px 0 40px;
    font-size: 13px;
    line-height: 18px;
  }
  .front__contact b { font-weight: 700; }

  /* Back */
  .back__band {
    position: absolute; left: 0; right: 0; top: 0; height: 80px;
    background: var(--brand-blue);
    border-bottom: 4px solid var(--brand-black);
    display: flex; align-items: center; padding-left: 40px; gap: 12px;
  }
  .back__band .company-dot { background: var(--brand-white); width: 28px; height: 28px; }
  .back__band .company-name { color: var(--brand-white); font-size: 24px; font-weight: 900; letter-spacing: 1px; }
  .back__watermark {
    position: absolute; left: 0; right: 0; top: 84px; bottom: 0;
    display: flex; align-items: center; justify-content: center;
  }
  .watermark-name {
    color: var(--watermark);
    font-weight: 900;
    font-size: 34px;
    letter-spacing: 2px;
    white-space: nowrap;
  }
</style>
</head>
<body>
  <section class="card card--front" aria-label="Business card front">
    <div class="front__building">
      <div class="building-name">ALDER CREEK</div>
      <div class="building-label">APARTMENTS</div>
    </div>
    <div class="front__company">
      <div class="company-dot"></div>
      <div class="company-name">HARROWGATE ESTATES</div>
    </div>
    <div class="front__nameband">
      <span class="manager-name">DANIEL WHITFIELD</span>
      <span class="manager-sep">|</span>
      <span class="manager-title">Property Manager</span>
    </div>
    <div class="front__contact">
      <div>2750 Alder Creek Road #B210</div>
      <div>Fresno, CA 93711</div>
      <div><b>Phone:</b> 555-214-7730 | <b>Fax:</b> 555-214-7731</div>
      <div><b>Email:</b> daniel@harrowgateestates.us</div>
      <div><b>www.harrowgateestates.us</b></div>
    </div>
  </section>

  <section class="card card--back" aria-label="Business card back">
    <div class="back__band">
      <div class="company-dot"></div>
      <div class="company-name">HARROWGATE ESTATES</div>
    </div>
    <div class="back__watermark">
      <div class="watermark-name">HARROWGATE ESTATES</div>
    </div>
  </section>
</body>
</html>
```